Web Design Project

My website was fine - years ago. But it's way, way overdue for an overhaul. When I started my business almost 20 years ago, I wanted to be edgy. And my website was just that. Color, style, voice. Edgy. Today, my clients are corporations. I'm older, more experienced - but still a little edgy. It's controlled edge. What I want now is sophisticated. Savvy. Corporate but cool. Grown up.

My clients are primarily - but not exclusively - in healthcare. But I don't want a healthcare site. I provide the following services:
1. Writing - white papers, brochures, web pages, speechwriting, etc.
2. Marketing strategy
3. Public relations services
4. Thought leader development
5. Training
I couldn't upload all the icons but I can send them. They correspond with the pages as follows and should be used in the design:

1. Writing- nib.png
2. Marketing strategy-compass.png
3. Public relations services-microphone.png
4. Thought leader development-lightbulb.png
5. Training: cogs-training.png or key.png

I will have a blog, and a portfolio of some kind.

I don't want something that looks like a template.
Updates

Reason: Just made this a committed payment. I apologize for not doing so from the start. Nobody should work for free.

Reason: Several folks have asked to resubmit, and it has taken me a while to provide feedback.

Dear Designers,

I am so sorry to have been so slow to select. I've had professional and personal issues to deal with. I am actively trying to select a design, however, and will do so in the next two days. Thanks so much for your patience and hard work.

Rhoda

Thanks so much to everyone who has submitted a design. I had great luck crowdsourcing my logo, but I'm starting to realize that website design is a totally different animal. All of your designs are great, but they all look exactly like templates. And maybe that's the way it's supposed to be, the way it should be. I don't want to use stock photography. It needs to be more personalized than that. I'm open to illustration or even using my own photo on the site, but stock photography won't work for me. If anyone wants to submit something else - and I understand if you don't - please feel free. 

Target Market(s)

C-suite executives; corporations, larger businesses who need marketing writing

Industry/Entity Type

Healthcare

Requirements
Must have
• Logo (somewhere)
Icons
Nice to have
• Level-specific page design (e.g, Home = Level 1, Tabs = Level 2, etc). I'd like it to have a certain order.

```html
<!DOCTYPE html>
<html lang="en">
<head>
<meta charset="utf-8">
<title>Corvell &amp; Co. — Home</title>
<link rel="stylesheet" href="https://fonts.googleapis.com/css2?family=Arimo:wght@400;700&family=Open+Sans:wght@400;600&family=Oswald:wght@600&display=swap">
<style>
  :root{
    --purple:#6b2c91;
    --orange:#f7941d;
    --nav-dark:#454545;
    --band-grey:#e6e6e6;
    --text-grey:#555;
    --text-dark:#333;
    --footer-link:#9a9a9a;
    --white:#fff;
    --card-grey:#dcdcdc;
  }
  *{margin:0;padding:0;box-sizing:border-box}
  html,body{width:1200px;height:1000px;overflow:hidden;background:var(--white)}
  body{position:relative;font-family:"Open Sans",sans-serif;color:var(--text-grey)}
  h2,h3,h4{font-weight:400}

  /* header */
  .site-header{position:absolute;left:0;top:0;width:1200px;height:120px;background:var(--white)}
  .brand{position:absolute;left:200px;top:66px;display:flex;align-items:center;gap:9px}
  .brand-dot{width:12px;height:12px;border-radius:50%;background:var(--purple)}
  .brand-name{font-family:"Arimo",sans-serif;font-weight:400;font-size:25px;color:var(--purple);line-height:1}
  .main-nav{position:absolute;left:308px;top:10px;width:673px;height:42px;background:var(--nav-dark);box-shadow:0 3px 6px rgba(0,0,0,.15)}
  .main-nav a{position:absolute;top:15px;transform:translateX(-50%);font-family:"Arimo",sans-serif;font-size:12px;color:var(--white);text-decoration:none;white-space:nowrap}
  .main-nav a.is-active{color:var(--orange);top:14px}
  .nav-active-bar{position:absolute;left:322px;top:52px;width:78px;height:4px;background:var(--orange)}

  /* hero */
  .hero{position:absolute;left:0;top:120px;width:1200px;height:290px;background:var(--band-grey)}
  .hero svg{position:absolute;left:0;top:0}
  .hero-title{position:absolute;left:461px;top:185px;font-family:"Arimo",sans-serif;font-size:29.5px;color:var(--purple);white-space:nowrap}
  .hero-sub{position:absolute;left:461px;top:216px;font-family:"Oswald",sans-serif;font-weight:600;font-size:28px;color:var(--orange);white-space:nowrap}

  /* services */
  .services{position:absolute;left:0;top:400px;width:1200px;height:186px}
  .services svg.edges{position:absolute;left:0;top:0}
  .service{position:absolute;top:28px;width:150px;transform:translateX(-50%);text-align:center}
  .service-icon{display:block;margin:0 auto}
  .service-title{margin-top:9px;font-family:"Arimo",sans-serif;font-size:12px;color:var(--orange);white-space:nowrap}
  .service-text{margin-top:3px;font-size:9px;line-height:12px;color:var(--text-dark)}
  .service-more{margin-top:8px;font-size:8.5px;color:var(--text-dark)}

  /* content */
  .content-area{position:absolute;left:0;top:586px;width:1200px;height:374px;background:var(--band-grey)}
  .content-panel{position:absolute;left:200px;top:27px;width:781px;height:327px;background:var(--white);border-radius:6px;box-shadow:0 6px 8px -4px rgba(0,0,0,.18)}
  .section-heading{position:absolute;font-family:"Arimo",sans-serif;font-size:15px;color:var(--purple)}
  .sub-heading{position:absolute;font-family:"Arimo",sans-serif;font-size:13px;color:var(--orange)}
  .body-copy{position:absolute;width:452px;font-size:9.2px;line-height:12px;color:var(--text-dark)}
  .panel-divider{position:absolute;left:468px;top:27px;width:1px;height:272px;background:#e2e2e2}

  .blog-card{position:absolute;left:484px;top:50px;width:276px;height:222px;background:var(--card-grey);border-radius:8px;box-shadow:0 6px 8px -4px rgba(0,0,0,.25)}
  .blog-inner{position:absolute;left:11px;top:11px;width:253px;height:197px;background:var(--white);border-radius:6px}
  .date-tag{position:absolute;left:-22px;top:16px;width:47px;height:32px;background:var(--orange);color:var(--white);text-align:center;font-family:"Arimo",sans-serif;font-weight:700;box-shadow:1px 2px 2px rgba(0,0,0,.25)}
  .date-tag .month{display:block;font-size:10px;line-height:11px;padding-top:3px}
  .date-tag .day{display:block;font-size:14px;line-height:15px}
  .date-fold{position:absolute;left:-22px;top:48px}
  .blog-title{position:absolute;left:46px;top:12px;width:200px;font-family:"Open Sans",sans-serif;font-size:18px;line-height:24px;color:#555}
  .blog-rule{position:absolute;left:10px;width:226px;height:1px;background:#ddd}
  .no-image{position:absolute;left:10px;top:78px;width:52px;height:52px;background:#e4e4e4;color:#bdbdbd;text-align:center;font-family:"Arimo",sans-serif;font-weight:700}
  .no-image .big{display:block;font-size:14px;padding-top:7px;line-height:14px}
  .no-image .small{display:block;font-size:7px;line-height:8px}
  .blog-excerpt{position:absolute;left:77px;top:79px;width:165px;font-size:9px;line-height:12px;color:var(--text-dark)}
  .blog-more{position:absolute;right:17px;top:133px;font-size:9px;color:#111}
  .blog-comments{position:absolute;left:10px;top:167px;display:flex;align-items:center;gap:5px;font-family:"Arimo",sans-serif;font-weight:700;font-size:10px;color:#222}

  /* footer */
  .site-footer{position:absolute;left:0;top:960px;width:1200px;height:40px;background:var(--nav-dark)}
  .footer-links{position:absolute;left:207px;top:16px;font-size:9px;color:var(--footer-link)}
  .footer-links span{margin:0 6px}
  .footer-copy{position:absolute;right:270px;top:16px;font-size:9px;color:var(--footer-link)}
</style>
</head>
<body>

<header class="site-header">
  <div class="brand">
    <span class="brand-dot"></span>
    <span class="brand-name">Corvell &amp; Co.</span>
  </div>
  <nav class="main-nav">
    <a class="is-active" style="left:57px">Home</a>
    <a style="left:138px">About Us</a>
    <a style="left:212px">Services</a>
    <a style="left:305px">Marketing Stretegy</a>
    <a style="left:393px">Training</a>
    <a style="left:462px">Contact Us</a>
  </nav>
  <div class="nav-active-bar"></div>
</header>

<section class="hero">
  <svg width="1200" height="290" viewBox="0 0 1200 290">
    <defs>
      <linearGradient id="metal" x1="0" y1="0" x2="1" y2="1">
        <stop offset="0" stop-color="#c9ccd1"/>
        <stop offset=".5" stop-color="#8d9196"/>
        <stop offset="1" stop-color="#d7dadd"/>
      </linearGradient>
    </defs>
    <polygon role="img" aria-label="Photo of interlocking silver puzzle pieces" points="200,1 981,1 812,170 372,170" fill="url(#metal)"/>
    <polygon role="img" aria-label="Photo of silver puzzle pieces, detail" points="200,245 274,172 455,172 385,245" fill="url(#metal)"/>
  </svg>
  <div class="hero-title">Winning Market Strategies</div>
  <div class="hero-sub">For Every Business</div>
</section>

<section class="services">
  <svg class="edges" width="1200" height="186" viewBox="0 0 1200 186">
    <defs>
      <pattern id="zig" width="10" height="6" patternUnits="userSpaceOnUse">
        <polygon points="0,6 5,0 10,6" fill="#fff"/>
      </pattern>
      <pattern id="zigDown" width="10" height="6" patternUnits="userSpaceOnUse">
        <polygon points="0,0 5,6 10,0" fill="#fff"/>
      </pattern>
    </defs>
    <rect x="0" y="0" width="1200" height="10" fill="#e6e6e6"/>
    <rect x="0" y="4" width="1200" height="6" fill="url(#zig)"/>
    <rect x="0" y="10" width="1200" height="170" fill="#fff"/>
    <rect x="0" y="180" width="1200" height="6" fill="#e6e6e6"/>
    <rect x="0" y="180" width="1200" height="6" fill="url(#zigDown)"/>
  </svg>

  <div class="service" style="left:261px">
    <svg class="service-icon" width="60" height="60" viewBox="0 0 60 60" role="img" aria-label="Writing icon">
      <circle cx="30" cy="30" r="28" fill="var(--purple)" stroke="var(--orange)" stroke-width="2"/>
      <path d="M20 40 L23 32 L37 18 L42 23 L28 37 Z" fill="none" stroke="#fff" stroke-width="1.6"/>
    </svg>
    <div class="service-title">Writing</div>
    <div class="service-text">Lorem ipsum dolor sit amet,<br>consectetuer adipiscing elit.</div>
    <div class="service-more">read more&gt;&gt;</div>
  </div>

  <div class="service" style="left:434px">
    <svg class="service-icon" width="60" height="60" viewBox="0 0 60 60" role="img" aria-label="Marketing strategy icon">
      <circle cx="30" cy="30" r="28" fill="var(--purple)" stroke="var(--orange)" stroke-width="2"/>
      <circle cx="30" cy="26" r="9" fill="none" stroke="#fff" stroke-width="1.6"/>
      <rect x="26" y="35" width="8" height="7" fill="var(--orange)"/>
    </svg>
    <div class="service-title">Marketing Strategy</div>
    <div class="service-text">Lorem ipsum dolor sit amet,<br>consectetuer adipiscing elit.</div>
    <div class="service-more">read more&gt;&gt;</div>
  </div>

  <div class="service" style="left:596px">
    <svg class="service-icon" width="60" height="60" viewBox="0 0 60 60" role="img" aria-label="Training icon">
      <circle cx="30" cy="30" r="28" fill="var(--purple)" stroke="var(--orange)" stroke-width="2"/>
      <circle cx="24" cy="34" r="7" fill="none" stroke="var(--orange)" stroke-width="3" stroke-dasharray="3 2"/>
      <circle cx="37" cy="23" r="6" fill="none" stroke="var(--orange)" stroke-width="3" stroke-dasharray="3 2"/>
    </svg>
    <div class="service-title">Training</div>
    <div class="service-text">Lorem ipsum dolor sit amet,<br>consectetuer adipiscing elit.</div>
    <div class="service-more">read more&gt;&gt;</div>
  </div>

  <div class="service" style="left:751px">
    <svg class="service-icon" width="60" height="60" viewBox="0 0 60 60" role="img" aria-label="Public relations icon">
      <circle cx="30" cy="30" r="28" fill="var(--purple)" stroke="var(--orange)" stroke-width="2"/>
      <circle cx="30" cy="30" r="15" fill="none" stroke="var(--orange)" stroke-width="1.4"/>
      <path d="M30 16 L33 30 L30 44 L27 30 Z M16 30 L30 27 L44 30 L30 33 Z" fill="var(--orange)"/>
    </svg>
    <div class="service-title">Public Relations Services</div>
    <div class="service-text">Lorem ipsum dolor sit amet,<br>consectetuer adipiscing elit.</div>
    <div class="service-more">read more&gt;&gt;</div>
  </div>

  <div class="service" style="left:917px">
    <svg class="service-icon" width="60" height="60" viewBox="0 0 60 60" role="img" aria-label="Leader development icon">
      <circle cx="30" cy="30" r="28" fill="var(--purple)" stroke="var(--orange)" stroke-width="2"/>
      <circle cx="30" cy="18" r="6" fill="none" stroke="var(--orange)" stroke-width="2"/>
      <path d="M30 24 V46 M30 40 H35 M30 44 H34" stroke="var(--orange)" stroke-width="2.4" fill="none"/>
    </svg>
    <div class="service-title">Leader Development</div>
    <div class="service-text">Lorem ipsum dolor sit amet,<br>consectetuer adipiscing elit.</div>
    <div class="service-more">read more&gt;&gt;</div>
  </div>
</section>

<section class="content-area">
  <div class="content-panel">
    <h2 class="section-heading" style="left:10px;top:20px">Welcome To Our Website</h2>
    <p class="body-copy" style="left:10px;top:52px">Lorem ipsum dolor sit amet, consectetuer adipiscing elit. Lorem ipsum dolor sit amet, consectetuer adipiscing elit.&nbsp; Lorem ipsum dolor sit amet, consectetuer adipiscing elit.&nbsp; Lorem ipsum dolor sit amet, consectetuer adipiscing elit. Lorem ipsum dolor sit amet, consectetuer adipiscing elit.</p>
    <p class="body-copy" style="left:10px;top:100px">Lorem ipsum dolor sit amet, consectetuer adipiscing elit. Lorem ipsum dolor sit amet, consectetuer adipiscing elit. Lorem ipsum dolor sit amet, consectetuer adipiscing elit. Lorem ipsum dolor sit amet, consectetuer adipiscing elit. Lorem ipsum dolor sit amet, consectetuer adipiscing elit. Lorem ipsum dolor sit amet, consectetuer adipiscing elit. Lorem ipsum dolor sit amet, consectetuer adipiscing elit.</p>
    <h3 class="sub-heading" style="left:9px;top:170px">Sub Heading</h3>
    <p class="body-copy" style="left:10px;top:196px">Lorem ipsum dolor sit amet, consectetuer adipiscing elit. Lorem ipsum dolor sit amet, consectetuer adipiscing elit. Lorem ipsum dolor sit amet, consectetuer adipiscing elit. Lorem ipsum dolor sit amet, consectetuer adipiscing elit.</p>

    <div class="panel-divider"></div>

    <h2 class="section-heading" style="left:489px;top:20px">Recent Blog Post</h2>
    <article class="blog-card">
      <div class="blog-inner">
        <div class="date-tag"><span class="month">AUG</span><span class="day">15</span></div>
        <svg class="date-fold" width="8" height="6" viewBox="0 0 8 6"><polygon points="0,0 8,0 8,6" fill="#b86a10"/></svg>
        <h4 class="blog-title">Lorem ipsum dolor sit amet</h4>
        <div class="blog-rule" style="top:68px"></div>
        <div class="no-image"><span class="big">NO</span><span class="big" style="padding-top:0">IMAGE</span><span class="small">AVAILABLE</span></div>
        <p class="blog-excerpt">Consectetuer adipiscing elit. Lorem ipsum dolor sit amet, consectetuer adipiscing elit. Lorem ipsum dolor sit amet, consectetuer adipiscing elit.</p>
        <div class="blog-more">&gt;&gt; read full post</div>
        <div class="blog-rule" style="top:161px"></div>
        <div class="blog-comments">
          <svg width="14" height="12" viewBox="0 0 14 12"><path d="M1 1 H13 V8 H6 L3 11 V8 H1 Z" fill="var(--orange)"/></svg>
          Comments
        </div>
      </div>
    </article>
  </div>
</section>

<footer class="site-footer">
  <div class="footer-links">Home<span>|</span>Terms and Conditions<span>|</span>Privacy Policy</div>
  <div class="footer-copy">All Right Reserved 2013.</div>
</footer>

</body>
</html>
```